Lumbrook - We create living space - needs a web/WIX design

The website will be in the German language.
During the contest, I welcome designs with English text.
I will provide the German text to the winner.
We prefer WIX-Design for the future, if possible to make the website WiX-ready;

The text to be used in the webpage:
In the project description I’ve written a text about our company in English and in German – as you asked for. Please use this text in the first step.

QUALITY, EXPERTISE and EXPERIENCE
EVERYTHING UNDER A SINGLE ROOF

We are a real estate company based in Vienna, Austria. Our company's main competences are planning, conception, development, erection, sale/renting and management of properties. "We make best quality for the best price" - with this motto LUMBROOK offers living space in high quality in Austria as well as in other countries. Thereby the working area of our property development focusses on both new construction and attic extensions.

QUALITÄT, KOMPETENZ UND ERFAHRUNG
ALLES UNTER EINEM DACH​

LUMBROOK ist ein Komplettanbieter für Wohnimmobilien von der Vision, Konzeption, Entwicklung, Planung, Errichtung und Verkauf/Vermietung bis zur Hausverwaltung. „Wir bauen beste Qualität zum besten Preis“, unter diesem Motto bietet LUMBROOK qualitativ hochwertigen, lebenswerten und nachhaltig gebauten Wohnraum sowohl in Österreich als auch in anderen Ländern an. Dabei konzentriert sich das Arbeitsfeld unserer Bauträgergesellschaft auf die beiden Kernbereiche Neubau und Dachgeschossausbau.

In the boxes “Must haves”, “Nice to haves”, “Should not haves” I’ve mentioned everything the designers need to know (font, colours etc.). AS I’ve received already some very good designs, there should be everything clear for the designers.

During the contest: homepage is welcome

Target Market(s)

Austria, Germany, Europe, Israel, USA; we would like to reach families, singles, male, female, general population and also investors

Industry/Entity Type

Real Estate Development

Number of Pages Required

5+ page

Font styles to use
Other font styles liked:
• See Upload

Colors

Designer to choose colors to be used in the design.

Requirements
Must have
• Pages called: "Company", "Projects", "Investments", "Partner", "Contact"; Link to projects; subsides (Team, News); enough space for renderings; Our company colours are yellow, grey, white and black (see our logo) - our website should be designed in this colours; Website in friendly and light colours
Nice to have
• Our company font for titles - attached; Eventually other font for the text - better readable; We prefer WIX-Design for the future, if possible to make the website WiX-ready.
• It should be clear, that the font in the attachement should be used; the provided files are pictures of our interior designs and the logo; we expect creativity from the designers, so they should use the best pictures in their opinion.
Should not have
• dark design

```html
<!DOCTYPE html>
<html lang="en">
<head>
<meta charset="utf-8">
<title>Lumbrook – We create living space</title>
<link rel="stylesheet" href="https://fonts.googleapis.com/css2?family=Aldrich&family=Open+Sans:wght@400;600;700&display=swap">
<style>
:root{
  --yellow:#fbf31c;
  --page:#efefef;
  --white:#ffffff;
  --ink:#222222;
  --text:#555555;
  --muted:#888888;
  --line:#dddddd;
}
*{box-sizing:border-box;margin:0;padding:0}
html,body{width:1200px;height:2894px;overflow:hidden}
body{background:var(--page);font-family:"Open Sans",sans-serif;color:var(--text);position:relative}

/* Navigation */
.site-header{position:absolute;left:35px;top:0;width:1130px;height:54px;display:flex;align-items:center;justify-content:space-between}
.brand{display:flex;align-items:center;gap:6px;font-family:"Aldrich",sans-serif;font-size:19px;color:var(--ink);letter-spacing:.5px}
.brand-square{width:9px;height:17px;background:var(--yellow)}
.main-nav{display:flex;gap:24px;font-family:"Aldrich",sans-serif;font-size:10px;color:var(--muted);letter-spacing:.4px;height:54px}
.main-nav a{color:inherit;text-decoration:none;display:flex;align-items:center}
.main-nav a.is-active{color:var(--ink);border-bottom:2px solid var(--ink);padding:0 10px}

/* Hero */
.hero{position:absolute;left:35px;top:54px;width:1130px;height:484px}
.hero-photo{position:absolute;inset:0;background:linear-gradient(120deg,#d9d4cc 0%,#c9b89c 35%,#e6e2da 55%,#9bb27a 75%,#eeeeea 100%)}
.hero-card{position:absolute;left:665px;top:102px;width:400px;height:282px;background:var(--yellow);padding:30px 30px}
.hero-title{font-family:"Aldrich",sans-serif;font-weight:400;font-size:27px;line-height:38px;color:var(--ink);letter-spacing:1px;white-space:nowrap}
.hero-title .soft{color:#555}
.btn-light{display:inline-block;margin-top:18px;background:var(--white);color:var(--ink);font-family:"Aldrich",sans-serif;font-size:12px;letter-spacing:1px;padding:12px 28px}

/* Panels */
.panel{position:absolute;left:35px;width:1130px;background:var(--white)}
.about{top:556px;height:156px;display:flex;align-items:center;padding:0 34px}
.about-heading{display:flex;align-items:center;gap:28px;width:300px;flex-shrink:0}
.about-mark{width:24px;height:24px;background:var(--yellow);flex-shrink:0}
.about-heading h2{font-family:"Aldrich",sans-serif;font-weight:400;font-size:28px;line-height:36px;letter-spacing:4px;color:var(--ink)}
.about p,.news p{font-size:14px;line-height:24px;color:var(--text)}
.about p strong,.news p strong{color:var(--ink)}

.section-title{display:flex;align-items:center;justify-content:center;gap:12px;font-family:"Aldrich",sans-serif;font-weight:400;font-size:27px;letter-spacing:4px;color:var(--ink)}
.marks{display:flex;gap:3px}
.marks i{display:block;width:11px;height:9px;background:var(--yellow)}

.projects-title{position:absolute;left:35px;top:770px;width:1130px}
.projects{position:absolute;left:35px;top:845px;width:1130px;height:363px;display:flex;gap:14px}
.project{position:relative;flex:1}
.project-photo{position:absolute;inset:0}
.project-photo.p1{background:linear-gradient(135deg,#2e5b6e 0%,#3f7488 45%,#dcdcdc 70%,#f2f2f2 100%)}
.project-photo.p2{background:linear-gradient(180deg,#b9d3e6 0%,#d7e4ec 35%,#b79b88 55%,#9a8879 75%,#c6c6bd 100%)}
.project-photo.p3{background:linear-gradient(120deg,#e4e0d8 0%,#8a6a4e 45%,#c8c2b8 65%,#9cbf72 100%)}
.btn-yellow{position:absolute;right:0;bottom:0;background:var(--yellow);color:var(--ink);font-family:"Aldrich",sans-serif;font-size:11px;padding:14px 20px}

.news{top:1223px;height:465px;text-align:center;padding-top:74px}
.news h3{margin:30px 0 8px;font-weight:400;font-size:27px;color:var(--ink)}
.news p{width:790px;margin:0 auto}
.news .place{font-size:9.5px;color:var(--muted);margin-top:6px}
.btn-outline{display:inline-block;margin-top:54px;border:2px solid var(--yellow);font-size:10px;color:var(--ink);padding:8px 18px}
.news-arrow{position:absolute;top:190px}
.news-arrow.prev{left:58px}
.news-arrow.next{right:58px}

.team{top:1705px;height:469px;padding-top:80px}
.team-list{display:flex;justify-content:center;gap:62px;margin-top:46px}
.member{width:118px;text-align:center}
.portrait{width:102px;height:102px;border-radius:50%;margin:0 auto 26px;background:radial-gradient(circle at 50% 40%,#cfcfcf,#9a9a9a)}
.portrait.dark{background:radial-gradient(circle at 50% 40%,#9e9e9e,#3a3a3a)}
.member h4{font-weight:600;font-size:15.5px;color:var(--ink);white-space:nowrap}
.member .role{font-size:9.5px;color:var(--muted);margin-top:2px;white-space:nowrap}
.member .rule{width:40px;height:2px;background:var(--ink);margin:9px auto 10px}
.member .contact{font-size:10px;line-height:17px;color:var(--muted);white-space:nowrap}

.request{top:2190px;height:503px;padding:70px 0 0 193px}
.request h2{font-family:"Aldrich",sans-serif;font-weight:400;font-size:26px;letter-spacing:6px;color:var(--ink);margin-bottom:18px;white-space:nowrap;width:727px}
.form-row{display:flex;gap:10px;margin-bottom:8px}
.field{border:1px solid var(--line);height:36px;font-size:9.5px;color:var(--muted);padding:0 18px;display:flex;align-items:center;width:727px}
.field.half{width:358.5px}
.field.message{height:138px}
.submit{width:727px;height:34px;border:2px solid var(--yellow);font-size:10px;font-weight:600;color:var(--ink);display:flex;align-items:center;justify-content:center;margin-top:10px}

/* Footer */
.site-footer{position:absolute;left:0;top:2693px;width:1200px;height:201px}
.footer-col{position:absolute;top:45px;font-size:10px;line-height:13px;color:var(--ink);white-space:nowrap}
.footer-col p{margin-bottom:9px}
.footer-brand{position:absolute;right:52px;top:44px;text-align:right}
.footer-brand .brand{justify-content:flex-end;font-size:18px}
.footer-brand .copy{font-size:9.5px;margin-top:6px;color:var(--ink)}
.social{display:flex;gap:14px;justify-content:flex-end;margin-top:26px}
.social span{width:11px;height:11px;border-radius:50%;background:var(--ink)}
</style>
</head>
<body>

<header class="site-header">
  <div class="brand"><span class="brand-square"></span>LUMBROOK</div>
  <nav class="main-nav">
    <a href="#" class="is-active">HOME</a>
    <a href="#">COMPANY</a>
    <a href="#">PROJECTS</a>
    <a href="#">INVESTMENTS</a>
    <a href="#">PARTNER</a>
    <a href="#">CONTACT US</a>
  </nav>
</header>

<section class="hero">
  <div class="hero-photo" role="img" aria-label="Rendering of a bright living and dining room with wooden table and garden view"></div>
  <div class="hero-card">
    <h1 class="hero-title">QUALITY, EXPERTISE<br>&amp; EXPERIENCE<br><span class="soft">EVERYTHING UNDER A<br>SINGLE ROOF</span></h1>
    <span class="btn-light">KNOW MORE</span>
  </div>
</section>

<section class="panel about">
  <div class="about-heading">
    <span class="about-mark"></span>
    <h2>ABOUT<br>COMPANY</h2>
  </div>
  <p>We are a real estate company based in Vienna, Austria. Our company's main competences are planning, conception, development, erection, sale/renting and management of properties. <strong>"We make best quality for the best price"</strong> - with this motto LUMBROOK offers living space in high quality in Austria as well as in other countries. Thereby the working area of our property development focusses on both new construction and attic extensions.</p>
</section>

<div class="projects-title">
  <h2 class="section-title"><span class="marks"><i></i><i></i><i></i></span>OUR PROJECTS<span class="marks"><i></i><i></i><i></i></span></h2>
</div>
<section class="projects">
  <article class="project">
    <div class="project-photo p1" role="img" aria-label="Rendering of a dining room with a teal wall and white chairs"></div>
    <span class="btn-yellow">KNOW MORE</span>
  </article>
  <article class="project">
    <div class="project-photo p2" role="img" aria-label="Rendering of a modern multi-storey residential building"></div>
    <span class="btn-yellow">KNOW MORE</span>
  </article>
  <article class="project">
    <div class="project-photo p3" role="img" aria-label="Rendering of a living room with wooden dining table"></div>
    <span class="btn-yellow">KNOW MORE</span>
  </article>
</section>

<section class="panel news">
  <h2 class="section-title"><span class="marks"><i></i><i></i><i></i></span>NEWS<span class="marks"><i></i><i></i><i></i></span></h2>
  <h3>BOLD DESIGN WOWS IN NORTH COOGEE</h3>
  <p>We are a real estate company based in Vienna, Austria. Our company's main competences are planning, conception, development, erection, sale/renting and management of properties. <strong>"We make best quality for the best price"</strong> - with this motto LUMBROOK offers living space in high quality in Austria as well as in other countries. Thereby the working area of our property development focusses on both new construction and attic extensions.</p>
  <p class="place">Western Australia</p>
  <span class="btn-outline">Know More</span>
  <svg class="news-arrow prev" width="30" height="60" viewBox="0 0 30 60" aria-hidden="true"><polyline points="28,2 2,30 28,58" fill="none" stroke="#aaa" stroke-width="2"/></svg>
  <svg class="news-arrow next" width="30" height="60" viewBox="0 0 30 60" aria-hidden="true"><polyline points="2,2 28,30 2,58" fill="none" stroke="#aaa" stroke-width="2"/></svg>
</section>

<section class="panel team">
  <h2 class="section-title"><span class="marks"><i></i><i></i><i></i></span>TEAM<span class="marks"><i></i><i></i><i></i></span></h2>
  <div class="team-list">
    <div class="member">
      <div class="portrait" role="img" aria-label="Portrait of Aaron Feld"></div>
      <h4>Aaron Feld</h4><p class="role">Chairman Managing Director</p><div class="rule"></div>
      <p class="contact">Tel: 555-010-2040<br>info@lumbrook.net</p>
    </div>
    <div class="member">
      <div class="portrait dark" role="img" aria-label="Portrait of Mira Castell"></div>
      <h4>Mira Castell</h4><p class="role">Chairman Managing Director</p><div class="rule"></div>
      <p class="contact">Tel: 555-010-2040<br>info@lumbrook.net</p>
    </div>
    <div class="member">
      <div class="portrait" role="img" aria-label="Portrait of Lukas Weidner"></div>
      <h4>Lukas Weidner</h4><p class="role">Chairman Managing Director</p><div class="rule"></div>
      <p class="contact">Tel: 555-010-2040<br>info@lumbrook.net</p>
    </div>
    <div class="member">
      <div class="portrait" role="img" aria-label="Portrait of Tomas Brandt"></div>
      <h4>Tomas Brandt</h4><p class="role">Chairman Managing Director</p><div class="rule"></div>
      <p class="contact">Tel: 555-010-2040<br>info@lumbrook.net</p>
    </div>
  </div>
</section>

<section class="panel request">
  <h2>FOR SPECIAL REQUESTS &amp; ORDERS</h2>
  <div class="form-row"><div class="field half">FIRSTNAME</div><div class="field half">EMAIL</div></div>
  <div class="form-row"><div class="field">SUBJECT</div></div>
  <div class="form-row"><div class="field message"></div></div>
  <div class="submit">SUBMIT</div>
</section>

<footer class="site-footer">
  <div class="footer-col" style="left:130px">
    <p>18 KOLBGASSE LANE<br>VIENNA 1030</p>
    <p>INFO@LUMBROOK.NET</p>
    <p>TEL: 555-010-2040<br>OPENING HOURS:</p>
    <p>MON - FRI: 7AM - 10PM</p>
  </div>
  <div class="footer-col" style="left:332px">
    <p>INFO@LUMBROOK.NET</p>
    <p>TEL: 555-010-2040</p>
  </div>
  <div class="footer-col" style="left:486px">
    <p>TEL: 555-010-2040</p>
    <p>OPENING HOURS:</p>
    <p>MON - FRI: 7AM - 10PM<br>SATURDAY: 8AM - 10PM<br>SUNDAY: 8AM - 11PM</p>
  </div>
  <div class="footer-brand">
    <div class="brand"><span class="brand-square"></span>LUMBROOK</div>
    <p class="copy">© 2023 LUMBROOK / ALL RIGHTS RESERVED.</p>
    <div class="social"><span></span><span></span><span></span></div>
  </div>
</footer>

</body>
</html>
```